Bordkarte MY Frelk
Unsere Ideen wurden sehr gut aufgenommen und in der Diskussion weiterentwickelt. Wir freuen uns, das Design einsetzen zu können
Zielgruppe
Bordkarte für ein Rentnerpaar, welches nahezu ganzjährig auf dem eigenen Motorschiff Nord- und Ostsee bereist.
Bei einer Bordkarte stehen Angaben zum Motorschiff im Fokus (Funkkennzeichen Identifikationsnummer)und nicht die des Eignerpaars das maximal mit Vornamen erscheint.
Die Karte wird anderen Eignern abgegeben und dient dazu, dass man sich auch auf grosse Distanzen suchen und kontaktieren kann. So wird bei diesen meist Einzelgängern das soziale Umfeld gepflegt.
Für nicht Berner, 'Frelk' ist Dialekt und bedeutet 'Bär'
Aufgabenstellung
Originelles*, maritimes Sujet oder markantes, nördliches Sternzeichen
(*keine Anker oder Muscheln!)
Maritimes Design, zurückhaltend, repräsentativ.
Die Karte soll das Gefühl der Ruhe und Zufriedenheit vermitteln
Schiff und Namesdesign als Bilder im Anhang. Die Rechte für das Wappen, habe ich einmalig für den Namen erworben.
MY Frelk
Henrike & Olaf
MMSI: 471.803.915
CS: KQRT7
InmarSat : 004926 81037

```html
<!DOCTYPE html>
<html lang="de">
<head>
<meta charset="utf-8">
<title>Bordkarte MY Frelk – Varianten 2.1 bis 2.4</title>
<link rel="stylesheet" href="https://fonts.googleapis.com/css2?family=Coustard:wght@900&family=Cormorant+Garamond:ital,wght@0,600;1,700&display=swap">
<style>
  :root {
    --page: #ffffff;
    --night: #00112a;
    --band: #3a5580;
    --title-blue: #5b8bd4;
    --white: #ffffff;
    --rose-grey: #858c98;
    --rose-blue: #2e4f80;
    --rose-ring: #5a6f90;
    --star: #f3f0b8;
    --label-ink: #111111;
  }
  * { margin: 0; padding: 0; box-sizing: border-box; }
  html, body {
    width: 861px; height: 1200px; overflow: hidden;
    background: var(--page);
  }
  .sheet { position: relative; width: 861px; height: 1200px; }

  .variant-label {
    position: absolute; left: 60px;
    font: 11px/1 "DejaVu Sans", Arial, sans-serif;
    color: var(--label-ink);
  }

  .card {
    position: absolute; left: 94px;
    width: 692px; height: 230px;
    background: var(--night);
    overflow: hidden;
  }
  .card__band {
    position: absolute; left: 0; top: 0;
    width: 40px; height: 100%;
    background: var(--band);
  }
  .card__artwork {
    position: absolute; right: 0; top: 0;
    width: 370px; height: 100%;
    background:
      radial-gradient(circle at 82% 78%, var(--rose-grey) 0%, var(--rose-blue) 22%, var(--rose-ring) 34%, rgba(90,111,144,0.35) 48%, rgba(0,17,42,0) 64%),
      radial-gradient(ellipse at 45% 40%, rgba(243,240,184,0.10) 0%, rgba(0,17,42,0) 60%);
  }

  .card__title {
    position: absolute; top: 6px;
    font-family: "Coustard", "Cooper Black", serif;
    font-weight: 900; font-size: 80px; line-height: 1;
    color: var(--title-blue);
    letter-spacing: 1px;
    white-space: nowrap;
  }
  .card__owners {
    position: absolute;
    font-family: "Cormorant Garamond", Georgia, serif;
    font-style: italic; font-weight: 700;
    font-size: 24px; line-height: 1;
    letter-spacing: 3px;
    color: var(--white);
    white-space: nowrap;
  }
  .card__details {
    position: absolute; top: 118px;
    font-family: "Cormorant Garamond", Georgia, serif;
    font-weight: 600; font-size: 27px; line-height: 31px;
  }
  .detail { display: flex; white-space: nowrap; }
  .detail__label { width: 133px; color: var(--title-blue); }
  .detail__value { color: var(--white); }

  /* Layout variants */
  .card--banded .card__title,
  .card--banded .card__details { left: 72px; }
  .card--banded .card__owners { left: 72px; top: 80px; }

  .card--plain-mid .card__title,
  .card--plain-mid .card__details { left: 55px; }
  .card--plain-mid .card__owners { left: 235px; top: 80px; }

  .card--plain-left .card__title,
  .card--plain-left .card__details { left: 31px; }
  .card--plain-left .card__owners { left: 211px; top: 80px; }
</style>
</head>
<body>
<main class="sheet">

  <section class="card card--banded" style="top:60px">
    <div class="card__band"></div>
    <div class="card__artwork" role="img" aria-label="Kompassrose mit Sternbild Großer Bär"></div>
    <h1 class="card__title">MY Frelk</h1>
    <p class="card__owners">Henrike &amp; Olaf</p>
    <dl class="card__details">
      <div class="detail"><dt class="detail__label">MMSI:</dt><dd class="detail__value">471.803.915</dd></div>
      <div class="detail"><dt class="detail__label">CS:</dt><dd class="detail__value">KQRT7</dd></div>
      <div class="detail"><dt class="detail__label">InmarSat:</dt><dd class="detail__value">004926 81037</dd></div>
    </dl>
  </section>
  <span class="variant-label" style="top:282px">2.1</span>

  <section class="card card--banded" style="top:336px">
    <div class="card__band"></div>
    <div class="card__artwork" role="img" aria-label="Kompassrose mit Sternbild Großer Bär"></div>
    <h1 class="card__title">MY Frelk</h1>
    <p class="card__owners">Henrike &amp; Olaf</p>
    <dl class="card__details">
      <div class="detail"><dt class="detail__label">MMSI:</dt><dd class="detail__value">471.803.915</dd></div>
      <div class="detail"><dt class="detail__label">CS:</dt><dd class="detail__value">KQRT7</dd></div>
      <div class="detail"><dt class="detail__label">InmarSat:</dt><dd class="detail__value">004926 81037</dd></div>
    </dl>
  </section>
  <span class="variant-label" style="top:558px">2.2</span>

  <section class="card card--plain-mid" style="top:612px">
    <div class="card__artwork" role="img" aria-label="Kompassrose mit Sternbild Großer Bär"></div>
    <h1 class="card__title">MY Frelk</h1>
    <p class="card__owners">Henrike &amp; Olaf</p>
    <dl class="card__details">
      <div class="detail"><dt class="detail__label">MMSI:</dt><dd class="detail__value">471.803.915</dd></div>
      <div class="detail"><dt class="detail__label">CS:</dt><dd class="detail__value">KQRT7</dd></div>
      <div class="detail"><dt class="detail__label">InmarSat:</dt><dd class="detail__value">004926 81037</dd></div>
    </dl>
  </section>
  <span class="variant-label" style="top:834px">2.3</span>

  <section class="card card--plain-left" style="top:887px">
    <div class="card__artwork" role="img" aria-label="Kompassrose mit Sternbild Großer Bär"></div>
    <h1 class="card__title">MY Frelk</h1>
    <p class="card__owners">Henrike &amp; Olaf</p>
    <dl class="card__details">
      <div class="detail"><dt class="detail__label">MMSI:</dt><dd class="detail__value">471.803.915</dd></div>
      <div class="detail"><dt class="detail__label">CS:</dt><dd class="detail__value">KQRT7</dd></div>
      <div class="detail"><dt class="detail__label">InmarSat:</dt><dd class="detail__value">004926 81037</dd></div>
    </dl>
  </section>
  <span class="variant-label" style="top:1109px">2.4</span>

</main>
</body>
</html>
```